Exciting Personal Development Book Cover: FIND ZEN NOW!

Design a Book Cover for my personal development book.
Title: Find Zen Now!
Author: Marcus Telly
Tagline: A real-life solution to get unstuck and break free

My picture must make up the front cover as I need to build my brand and people should recognise me on book shelves. Bold and catchy. How you do it is up to you. There must be space for a short testimonial from a famous person who is currently reading my book. I uploaded a sample of what I made in Photoshop but I don't have design skills.

I've added a PDF of my book so you can read the chapter index and introduction to get a sense of the content.

Target Market(s)

Personal Development Self-Help Market

Industry/Entity Type

Personal Development

Font styles to use
Serif
Sans Serif

Requirements
Must have
• My picture as hero image on cover.
Nice to have
• Must have Title, Tagline and my author name. If possible ZEN stands for 'Zeal, Energy & Nerve' If there is a way to fit this somewhere great. If it's too much then it can go somewhere on the back.

```html
<!DOCTYPE html>
<html lang="en">
<head>
<meta charset="utf-8">
<title>Find Zen Now! – Book Cover</title>
<link rel="stylesheet" href="https://fonts.googleapis.com/css2?family=Bebas+Neue&family=Montserrat:wght@300;500;700&display=swap">
<style>
  :root {
    --page-bg: #f7f7f7;
    --cover-top: #5b6369;
    --cover-mid: #646c73;
    --cover-bottom: #545b61;
    --frame: #ffffff;
    --ink-light: #ffffff;
    --ink-dark: #3f4448;
    --photo-light: #e9e6e2;
    --photo-mid: #b9b4ae;
    --photo-dark: #7c7570;
  }
  * { margin: 0; padding: 0; box-sizing: border-box; }
  html, body {
    width: 704px;
    height: 1200px;
    overflow: hidden;
    background: var(--page-bg);
  }
  .book-cover {
    position: absolute;
    left: 0;
    top: 104px;
    width: 704px;
    height: 992px;
    background: linear-gradient(180deg, var(--cover-top) 0%, var(--cover-mid) 45%, var(--cover-bottom) 100%);
    box-shadow: 0 2px 6px rgba(0,0,0,0.18);
    overflow: hidden;
  }
  .frame-bar {
    position: absolute;
    background: var(--frame);
  }
  .frame-top    { left: 96px;  top: 93px;  width: 497px; height: 27px; }
  .frame-right  { left: 566px; top: 93px;  width: 27px;  height: 652px; }
  .frame-bottom { left: 96px;  top: 718px; width: 497px; height: 27px; }
  .frame-left-upper { left: 96px; top: 93px;  width: 27px; height: 78px; }
  .frame-left-lower { left: 96px; top: 553px; width: 27px; height: 192px; }

  .author-photo {
    position: absolute;
    left: 248px;
    top: 138px;
    width: 355px;
    height: 580px;
    background:
      radial-gradient(ellipse 28% 16% at 48% 20%, var(--photo-dark) 0%, rgba(124,117,112,0) 100%),
      radial-gradient(ellipse 60% 55% at 52% 62%, var(--photo-light) 0%, var(--photo-mid) 75%, rgba(185,180,174,0) 100%);
  }

  .title {
    position: absolute;
    left: 99px;
    top: 172px;
    font-family: "Bebas Neue", "Oswald", sans-serif;
    font-size: 140px;
    line-height: 122px;
    color: var(--ink-light);
    letter-spacing: 0.5px;
  }
  .title span { display: block; }

  .acronym {
    position: absolute;
    left: 152px;
    top: 620px;
    font-family: "Montserrat", sans-serif;
    font-weight: 300;
    font-size: 19px;
    line-height: 24px;
    color: var(--ink-light);
    letter-spacing: 0.5px;
  }
  .acronym span { display: block; }

  .tagline-rule {
    position: absolute;
    left: 96px;
    top: 764px;
    width: 9px;
    height: 76px;
    background: var(--frame);
  }
  .tagline {
    position: absolute;
    left: 119px;
    top: 768px;
    font-family: "Montserrat", sans-serif;
    font-size: 29px;
    line-height: 38px;
    color: var(--ink-light);
    letter-spacing: 0.6px;
  }
  .tagline-lead { display: block; font-weight: 300; }
  .tagline-punch { display: block; font-weight: 500; }
  .tagline-punch .connector { font-weight: 300; }

  .author-name {
    position: absolute;
    left: 260px;
    top: 957px;
    width: 185px;
    height: 36px;
    background: var(--frame);
    font-family: "Montserrat", sans-serif;
    font-weight: 700;
    font-size: 21px;
    line-height: 36px;
    text-align: center;
    color: var(--ink-dark);
  }
</style>
</head>
<body>
  <main class="book-cover">
    <div class="author-photo" role="img" aria-label="Portrait of the author, smiling, in a white shirt with tattooed forearms crossed"></div>

    <div class="frame-bar frame-top"></div>
    <div class="frame-bar frame-right"></div>
    <div class="frame-bar frame-bottom"></div>
    <div class="frame-bar frame-left-upper"></div>
    <div class="frame-bar frame-left-lower"></div>

    <h1 class="title">
      <span>FIND</span>
      <span>ZEN</span>
      <span>NOW!</span>
    </h1>

    <p class="acronym">
      <span>Zeal</span>
      <span>Energy</span>
      <span>Nerve</span>
    </p>

    <div class="tagline-rule"></div>
    <p class="tagline">
      <span class="tagline-lead">A real-life solution to get</span>
      <span class="tagline-punch">UNSTUCK <span class="connector">and</span> BREAK FREE</span>
    </p>

    <p class="author-name">Marcus Telly</p>
  </main>
</body>
</html>
```